New National Dermatology Group needs a business card!

We need a business card for our new national company that has 3 brands within the business:
Brindlewood Clinics Australia, Harrowmere Clinics Australia and Tallowfen Clinics Australia.
We help people access dermatology services close to home throughout Australia.
We need a business card that has:
all 3 logos on it,
Our websites (there are three, listed above)
Our email (there are three, listed above)
The location of our first clinic: 41 Wren St Parramatta (this can then be changed for each location as required)

```html
<!DOCTYPE html>
<html lang="en">
<head>
<meta charset="utf-8">
<title>Business Card – Brindlewood, Harrowmere &amp; Tallowfen Clinics Australia</title>
<link rel="stylesheet" href="https://fonts.googleapis.com/css2?family=EB+Garamond:wght@400;500&display=swap">
<style>
  :root {
    --page-bg: #e6e6e6;
    --card-white: #ffffff;
    --orange-top: #ea8506;
    --orange-bottom: #e8720b;
    --green-top: #07b359;
    --green-bottom: #04a846;
    --brown-top: #8b5634;
    --brown-bottom: #6b3205;
    --ink-light: #f4f1ec;
    --ink-dark: #3a3a3a;
    --map-grey: #e7e8ea;
    --map-tone: #d9dcdf;
    --card-shadow: 0 10px 28px rgba(0, 0, 0, 0.18);
  }

  * { margin: 0; padding: 0; box-sizing: border-box; }

  html, body {
    width: 1200px;
    height: 900px;
    overflow: hidden;
    background: var(--page-bg);
    font-family: "EB Garamond", Garamond, serif;
  }

  .canvas {
    width: 1200px;
    height: 900px;
    display: flex;
    flex-direction: column;
    align-items: center;
    justify-content: center;
    gap: 40px;
  }

  .card {
    width: 640px;
    height: 366px;
    box-shadow: var(--card-shadow);
    position: relative;
    overflow: hidden;
  }

  /* Back side: white with brand names, map and address */
  .card-back { background: var(--card-white); }

  .brand-list {
    position: absolute;
    left: 36px;
    top: 60px;
    display: flex;
    flex-direction: column;
    gap: 22px;
  }

  .brand-mini {
    font-size: 18px;
    font-weight: 400;
    line-height: 1.2;
    color: var(--ink-dark);
    white-space: nowrap;
  }

  .location-map {
    position: absolute;
    right: 30px;
    top: 62px;
    width: 330px;
    height: 214px;
    background: linear-gradient(135deg, var(--map-grey), var(--map-tone));
  }

  .clinic-address {
    position: absolute;
    left: 36px;
    bottom: 34px;
    font-size: 19px;
    color: var(--ink-dark);
  }

  /* Front side: three coloured brand bands */
  .card-front {
    display: flex;
    flex-direction: column;
  }

  .brand-band {
    flex: 1;
    display: flex;
    align-items: center;
    padding: 0 0 0 44px;
    color: var(--ink-light);
  }
  .brand-band.harrowmere { background: linear-gradient(180deg, var(--orange-top), var(--orange-bottom)); }
  .brand-band.brindlewood { background: linear-gradient(180deg, var(--green-top), var(--green-bottom)); }
  .brand-band.tallowfen { background: linear-gradient(180deg, var(--brown-top), var(--brown-bottom)); }

  .brand-title {
    width: 300px;
    font-size: 23px;
    font-weight: 400;
    line-height: 1.2;
    white-space: nowrap;
  }

  .brand-contact {
    margin-left: 12px;
    font-size: 16px;
    line-height: 1.5;
    white-space: nowrap;
  }
</style>
</head>
<body>
  <main class="canvas">

    <section class="card card-back" aria-label="Business card, back">
      <div class="brand-list">
        <p class="brand-mini">Harrowmere Clinics Australia</p>
        <p class="brand-mini">Brindlewood Clinics Australia</p>
        <p class="brand-mini">Tallowfen Clinics Australia</p>
      </div>

      <div class="location-map" role="img" aria-label="Street map of Parramatta showing the clinic location at 41 Wren St"></div>

      <p class="clinic-address">41 Wren St Parramatta NSW 2150</p>
    </section>

    <section class="card card-front" aria-label="Business card, front">
      <div class="brand-band harrowmere">
        <p class="brand-title">Harrowmere Clinics Australia</p>
        <p class="brand-contact">harrowmereclinics.com.au<br>email@harrowmereclinics.com.au</p>
      </div>
      <div class="brand-band brindlewood">
        <p class="brand-title">Brindlewood Clinics Australia</p>
        <p class="brand-contact">brindlewoodclinics.com.au<br>email@brindlewoodclinics.com.au</p>
      </div>
      <div class="brand-band tallowfen">
        <p class="brand-title">Tallowfen Clinics Australia</p>
        <p class="brand-contact">tallowfenclinics.com.au<br>email@tallowfenclinics.com.au</p>
      </div>
    </section>

  </main>
</body>
</html>
```